Molar Bridgeworks Business Card Design

I need a business card design for a renamed company. The company is Molar Bridgeworks.

The design concept is to communicate clean simplicity, clarity, professionalism but also a touch of innovation. That is also our company concept.

** Please note: I've attached my initial design for your review. You don't have to follow that exactly, but I do want you to see what I'm thinking.

Also, I've attached our logo but it's in a format that's probably not good enough for the final product. I can send an updated one later, but this can get you going....

Target Market(s)

CEOs, CFOs, Vice Presidents of Supply Chain, Surgeons

Industry/Entity Type

Business

Requirements
Must have
• White background
• Use font that complements or is similar to our logo
• Minimal type on the front - just the basics
• Use colors: PMS 186 Red, PMS 430 Gray, and PMS 296 Blue
• Back side should be in the Gray or Blue color above - I'm open to which one. But if it's the Gray color it may accommodate someone writing on it better....
Nice to have
• Rounded edges (or some way to add extra or unexpected detail
• Satin-type finish - communicates quality

```html
<!DOCTYPE html>
<html lang="en">
<head>
<meta charset="utf-8">
<title>Molar Bridgeworks Business Card</title>
<link rel="stylesheet" href="https://fonts.googleapis.com/css2?family=Cousine:wght@400;700&display=swap">
<style>
  :root {
    --backdrop: #2b2b2d;
    --card-white: #f7f8f8;
    --pms-186-red: #d22a3c;
    --pms-430-gray: #8e989c;
    --pms-296-blue: #14244a;
    --ink: #2a2a2a;
    --contact-teal: #1d5566;
    --mono: "Cousine", monospace;
  }
  html, body {
    margin: 0;
    padding: 0;
    width: 1200px;
    height: 900px;
    overflow: hidden;
    background: var(--backdrop);
    font-family: var(--mono);
  }
  .stage {
    position: relative;
    width: 1200px;
    height: 900px;
  }
  .card {
    position: absolute;
    width: 520px;
    height: 300px;
    border-radius: 24px;
    overflow: hidden;
    box-shadow: 0 14px 36px rgba(0,0,0,0.45);
  }
  .card-shape {
    position: absolute;
    inset: 0;
    width: 100%;
    height: 100%;
  }

  /* Back side */
  .card-back {
    left: 120px;
    top: 130px;
    background: var(--pms-430-gray);
  }
  .tagline {
    position: absolute;
    left: 30px;
    top: 34px;
    width: 400px;
    margin: 0;
    text-align: center;
    color: var(--pms-186-red);
    font-size: 21px;
    line-height: 1.3;
    font-weight: 400;
  }
  .back-contact {
    position: absolute;
    left: 52px;
    top: 188px;
    margin: 0;
    color: var(--contact-teal);
    font-size: 17px;
    line-height: 1.25;
    font-style: normal;
  }
  .back-contact .web { font-weight: 700; }
  .back-note {
    position: absolute;
    right: 28px;
    bottom: 22px;
    margin: 0;
    color: var(--contact-teal);
    font-size: 14px;
  }

  /* Front side */
  .card-front {
    left: 560px;
    top: 430px;
    background: var(--card-white);
  }
  .wordmark {
    position: absolute;
    left: 34px;
    top: 44px;
    display: flex;
    align-items: center;
    gap: 10px;
    margin: 0;
  }
  .wordmark-dot {
    width: 12px;
    height: 12px;
    border-radius: 50%;
    background: var(--pms-186-red);
  }
  .wordmark-name {
    color: var(--pms-296-blue);
    font-size: 30px;
    font-weight: 700;
    letter-spacing: -0.5px;
  }
  .person {
    position: absolute;
    left: 34px;
    top: 130px;
    margin: 0;
  }
  .person-name {
    display: block;
    color: var(--pms-186-red);
    font-size: 22px;
    line-height: 1.2;
  }
  .person-title {
    display: block;
    color: var(--ink);
    font-size: 17px;
    line-height: 1.3;
  }
  .front-contact {
    position: absolute;
    left: 34px;
    top: 210px;
    margin: 0;
    color: var(--ink);
    font-size: 17px;
    line-height: 1.35;
    font-style: normal;
  }
</style>
</head>
<body>
<main class="stage">

  <section class="card card-back" aria-label="Card back">
    <svg class="card-shape" viewBox="0 0 520 300" aria-hidden="true">
      <path d="M0 0 H520 V20 Q330 150 0 175 Z" fill="var(--card-white)"/>
    </svg>
    <p class="tagline">“Precise Care, Made Simple<br>For Every Practice”</p>
    <address class="back-contact">
      <span class="web">www.molarbridgeworks.com</span><br>
      4120 Harbor Lane<br>
      Brookfield TN 38000<br>
      555.872.0190
    </address>
    <p class="back-note">A Member Company</p>
  </section>

  <section class="card card-front" aria-label="Card front">
    <svg class="card-shape" viewBox="0 0 520 300" aria-hidden="true">
      <circle cx="548" cy="300" r="195" fill="var(--pms-296-blue)"/>
    </svg>
    <h1 class="wordmark">
      <span class="wordmark-dot"></span>
      <span class="wordmark-name">Molar Bridgeworks</span>
    </h1>
    <p class="person">
      <span class="person-name">Dana Morrow</span>
      <span class="person-title">VP and Lead Partner</span>
    </p>
    <address class="front-contact">
      morrow@molarbridgeworks.com<br>
      555.326.0142&nbsp;&nbsp;C
    </address>
  </section>

</main>
</body>
</html>
```